Apartment Investor Business Card Design

Need a new business card designed for my multifamily investment company

Industry/Entity Type

Real Estate

Contact Information for Business Card

Garrick Pelham - President & CEO
Brightwold Holdings, LLC
4838 North 92nd Avenue, Ste 500
Omaha, NE 68999
(402) 555-0147
Garrick@brightwoldholdings.example
Www.BrightwoldHoldings.example

Colors
3176b5

```html
<!DOCTYPE html>
<html lang="en">
<head>
<meta charset="utf-8">
<title>Brightwold Holdings – Business Card</title>
<link rel="stylesheet" href="https://fonts.googleapis.com/css2?family=Roboto:wght@400;500;700&display=swap">
<style>
  :root {
    --page-bg: #e9e9e7;
    --card-dark: #1c1d20;
    --brand-blue: #4f86c6;
    --text-white: #ffffff;
    --text-gray: #8a8b8d;
    --divider: #6d6e70;
  }
  * { margin: 0; padding: 0; box-sizing: border-box; }
  html, body {
    width: 1125px;
    height: 1200px;
    overflow: hidden;
    background: var(--page-bg);
    font-family: "Roboto", Arial, sans-serif;
  }
  .canvas { position: relative; width: 1125px; height: 1200px; }

  .card {
    position: absolute;
    left: 150px;
    width: 825px;
    height: 472px;
    overflow: hidden;
  }
  .card--front { top: 98px; background: var(--card-dark); }
  .card--back { top: 632px; background: var(--brand-blue); }

  .brand-name {
    position: absolute;
    left: 0;
    right: 0;
    text-align: center;
    color: var(--text-white);
    font-weight: 400;
    text-transform: uppercase;
    white-space: nowrap;
  }
  .card--front .brand-name { top: 160px; font-size: 36px; letter-spacing: 2px; }
  .card--back .brand-name { top: 272px; font-size: 44px; letter-spacing: 2px; }

  .person {
    position: absolute;
    right: 509px;
    top: 275px;
    text-align: right;
  }
  .person__name {
    color: var(--brand-blue);
    font-weight: 700;
    font-size: 31px;
    line-height: 36px;
    white-space: nowrap;
  }
  .person__title {
    color: var(--text-gray);
    font-weight: 500;
    font-size: 20px;
    line-height: 24px;
  }

  .divider {
    position: absolute;
    left: 340px;
    top: 230px;
    width: 2px;
    height: 145px;
    background: var(--divider);
  }

  .contact {
    position: absolute;
    left: 366px;
    top: 234px;
    color: var(--text-white);
    font-size: 20px;
    line-height: 25px;
    white-space: nowrap;
  }
  .contact__company { font-weight: 700; }
  .contact__lines { margin-bottom: 10px; }
  .contact__row { display: flex; align-items: center; gap: 10px; line-height: 27px; }
  .contact__icon { width: 18px; height: 18px; fill: var(--brand-blue); flex: none; }

  .web-band {
    position: absolute;
    left: 0;
    top: 406px;
    width: 738px;
    height: 43px;
    background: var(--brand-blue);
    clip-path: polygon(0 0, 100% 0, 94% 100%, 0 100%);
    color: var(--text-white);
    font-size: 19px;
    letter-spacing: 3.4px;
    line-height: 43px;
    padding-left: 162px;
    white-space: nowrap;
  }
</style>
</head>
<body>
<main class="canvas">

  <section class="card card--front" aria-label="Business card front">
    <p class="brand-name">Brightwold Holdings</p>

    <div class="person">
      <p class="person__name">Garrick Pelham</p>
      <p class="person__title">President &amp; CEO</p>
    </div>

    <div class="divider"></div>

    <div class="contact">
      <div class="contact__lines">
        <p class="contact__company">Brightwold Holdings, LLC</p>
        <p>4838 North 92nd Avenue, Ste 500</p>
        <p>Omaha, NE 68999</p>
      </div>
      <p class="contact__row">
        <svg class="contact__icon" viewBox="0 0 24 24" aria-hidden="true"><path d="M6.6 10.8a15.2 15.2 0 0 0 6.6 6.6l2.2-2.2a1 1 0 0 1 1-.25 11.4 11.4 0 0 0 3.6.57 1 1 0 0 1 1 1V20a1 1 0 0 1-1 1A17 17 0 0 1 3 4a1 1 0 0 1 1-1h3.5a1 1 0 0 1 1 1c0 1.25.2 2.45.57 3.57a1 1 0 0 1-.25 1z"/></svg>
        (402) 555-0147
      </p>
      <p class="contact__row">
        <svg class="contact__icon" viewBox="0 0 24 24" aria-hidden="true"><path d="M2 5h20v14H2z M2 5l10 8 10-8" fill="var(--brand-blue)"/><path d="M2 5l10 8 10-8" fill="none" stroke="var(--card-dark)" stroke-width="1.6"/></svg>
        Garrick@brightwoldholdings.example
      </p>
    </div>

    <p class="web-band">Www.BrightwoldHoldings.example</p>
  </section>

  <section class="card card--back" aria-label="Business card back">
    <p class="brand-name">Brightwold Holdings</p>
  </section>

</main>
</body>
</html>
```